When the boots match march on! book cover design

Book cover for a business, non-fiction book.
About stepping up, being who you truly are, and willing not to fit in.

TITLE: When The Boots Match, March On!
SUBTITLE: Quit copying the chief others expect of you and begin shaping the chief nobody else could ever shape...
AUTHOR: Tobias Hartwell-Brenner
Updates

we never uploaded the brief

Target Market(s)

Business people, curious leaders, insiders who have a secret itch to be an outsider
AGE: 35-50 years old

Font styles to use
Sans Serif
Other font styles liked:
• designer's choice!

Requirements
Must have
• Very visual
Imagery must reflect the topic of the book

```html
<!DOCTYPE html>
<html lang="en">
<head>
<meta charset="utf-8">
<title>When The Boots Match, March On! — Book Cover</title>
<link rel="stylesheet" href="https://fonts.googleapis.com/css2?family=Fira+Sans:wght@300;400;900&display=swap">
<style>
  :root {
    --page: #ffffff;
    --cover: #f1f1f1;
    --title: #1b2238;
    --subtitle: #8a2b17;
    --author: #222222;
  }
  html, body {
    margin: 0;
    padding: 0;
    width: 1200px;
    height: 1200px;
    overflow: hidden;
    background: var(--page);
  }
  .canvas {
    position: relative;
    width: 1200px;
    height: 1200px;
    background: var(--page);
  }
  .cover {
    position: absolute;
    left: 200px;
    top: 0;
    width: 800px;
    height: 1200px;
    background: var(--cover);
    font-family: "Fira Sans", Arial, sans-serif;
    text-align: center;
  }
  .cover-art {
    position: absolute;
    left: 280px;
    top: 40px;
    width: 320px;
    height: 460px;
  }
  .title {
    position: absolute;
    left: 0;
    right: 0;
    top: 533px;
    margin: 0;
    font-weight: 900;
    font-size: 100px;
    line-height: 108px;
    color: var(--title);
    text-transform: uppercase;
    letter-spacing: 0.01em;
  }
  .title span { display: block; }
  .subtitle {
    position: absolute;
    left: 0;
    right: 0;
    top: 905px;
    margin: 0;
    font-weight: 400;
    font-size: 29px;
    line-height: 42px;
    letter-spacing: 0.07em;
    color: var(--subtitle);
    text-transform: uppercase;
  }
  .subtitle span { display: block; }
  .author {
    position: absolute;
    left: 0;
    right: 0;
    top: 1088px;
    margin: 0;
    font-weight: 300;
    font-size: 36px;
    letter-spacing: 0.05em;
    color: var(--author);
    text-transform: uppercase;
  }
</style>
</head>
<body>
  <div class="canvas">
    <div class="cover">
      <svg class="cover-art" viewBox="0 0 320 460" role="img" aria-label="Illustration of a bunch of colourful balloons on strings lifting a brown leather briefcase into the air">
        <defs>
          <linearGradient id="artTones" x1="0" y1="0" x2="0" y2="1">
            <stop offset="0" stop-color="#e4463f"/>
            <stop offset="0.1" stop-color="#d94fa8"/>
            <stop offset="0.2" stop-color="#5d9be0"/>
            <stop offset="0.3" stop-color="#8e5ad0"/>
            <stop offset="0.42" stop-color="#dcdcdc"/>
            <stop offset="0.7" stop-color="#dcdcdc"/>
            <stop offset="0.8" stop-color="#9a4a28"/>
            <stop offset="0.95" stop-color="#6e3119"/>
            <stop offset="1" stop-color="#e2e2e2"/>
          </linearGradient>
        </defs>
        <rect x="0" y="0" width="320" height="460" rx="60" fill="url(#artTones)" opacity="0.85"/>
      </svg>

      <h1 class="title">
        <span>When The</span>
        <span>Boots Match,</span>
        <span>March On!</span>
      </h1>

      <p class="subtitle">
        <span>Quit copying the chief others</span>
        <span>expect of you and begin</span>
        <span>shaping the chief nobody else</span>
        <span>could ever shape...</span>
      </p>

      <p class="author">Tobias Hartwell-Brenner</p>
    </div>
  </div>
</body>
</html>
```